Precise Finish Emulator (PFE)

I would like to design a dedicated site for my PFE product, which allows industry employees to be trained in the visual inspection of mechanical parts. My product is a 3D simulator (see https://norvik-works.ch/our-applications/virtual-reality/ and https://norvik-works.ch for videos) which makes it possible to manufacture standard parts representative of a type of defect which is accepted or refused by the quality department. These master parts can be used to create a common quality culture in the company and to train employees in a homogeneous way. The simulator is initially designed for watchmaking, but must be designed for much broader industries (cars, phone reconditioning, ball bearings, etc.)
L'information que j'ai donnée n'est pas assez précise. Je dois préciser les domaines métiers visés par le site internet. J'ai besoin de quelques jours pour choisir les domaines les plus représentatifs.

```html
<!DOCTYPE html>
<html lang="en">
<head>
<meta charset="utf-8">
<title>Precise Finish Emulator</title>
<link href="https://fonts.googleapis.com/css2?family=League+Spartan:wght@500;600;700&family=Roboto:wght@400;500;700&display=swap" rel="stylesheet">
<style>
:root{
  --blue:#0f6cbd;
  --blue-dark:#0a5aa3;
  --navy:#1b2535;
  --ink:#1d1d22;
  --text:#444a55;
  --pale:#f1f6fc;
  --white:#ffffff;
}
*{box-sizing:border-box;margin:0;padding:0}
html,body{width:1200px;height:5226px;overflow:hidden}
body{position:relative;background:var(--white);font-family:'Roboto',sans-serif;color:var(--text)}
.abs{position:absolute}
h1,h2,h3,.brand{font-family:'League Spartan',sans-serif;color:var(--ink);font-weight:600}
.shapes{position:absolute;left:0;top:0}

/* header */
.brand{left:112px;top:12px;font-size:36px;line-height:40px}
.phone-top{right:112px;top:18px;display:flex;align-items:center;gap:12px;font-size:14px;color:var(--ink)}
.icon-circle{width:32px;height:32px;border-radius:50%;background:var(--blue);display:flex;align-items:center;justify-content:center}
.nav{left:0;top:72px;width:1200px;height:54px}
.nav-links{left:100px;top:72px;height:54px;display:flex;align-items:center;gap:0;font-size:14px;color:#fff;text-transform:uppercase}
.nav-links span{padding:0 22px;position:relative}
.nav-links span+span::before{content:"|";position:absolute;left:-3px}
.nav-links .active{border-bottom:3px solid #fff;padding-bottom:14px;padding-top:17px;margin-top:0}
.login{left:978px;top:72px;height:54px;display:flex;align-items:center;gap:10px;font-size:14px;font-weight:700;color:#fff}

/* hero */
.hero-title{left:106px;top:250px;font-size:66px;line-height:72px;color:#fff;font-weight:700}
.hero-sub{left:106px;top:414px;font-size:30px;line-height:46px;color:#fff;font-family:'Roboto',sans-serif;font-weight:500}
.btn{background:var(--blue);color:#fff;font-weight:700;display:flex;align-items:center;justify-content:center;gap:12px;border-radius:3px}
.hero-btn{left:106px;top:538px;width:184px;height:64px;font-size:19px}

/* control */
.control-head{left:595px;top:910px;font-size:42px;line-height:48px}
.ticks{left:595px;top:1024px;width:492px;list-style:none;font-size:14.5px;line-height:26px}
.ticks li{position:relative;padding-left:28px;margin-bottom:16px;text-align:justify}
.ticks li::before{content:"";position:absolute;left:0;top:6px;width:14px;height:14px;border-radius:50%;background:var(--blue)}
.ticks li::after{content:"";position:absolute;left:4px;top:9px;width:5px;height:7px;border:solid #fff;border-width:0 2px 2px 0;transform:rotate(45deg)}

.center-head{width:1200px;left:0;text-align:center;font-size:42px;line-height:48px}
.para{font-size:15px;line-height:26px}

.band-text{left:230px;width:740px;text-align:center;color:#fff;font-size:15px;line-height:26px}

/* cards */
.card{background:#fff;box-shadow:0 6px 24px rgba(20,40,80,.18);text-align:center;font-size:13.5px;line-height:21px;padding:0 16px}
.card svg{display:block;margin:26px auto 18px}

.story-card{background:#fff;box-shadow:0 8px 30px rgba(20,40,80,.18)}
.story-card h3{text-align:center;font-size:25px;line-height:30px;margin-top:20px}
.story-card .more{display:flex;justify-content:center;align-items:center;gap:10px;color:var(--blue);font-weight:700;font-size:18px;margin-top:14px}

/* footer */
.footer{left:0;top:4706px;width:1200px;height:462px;background:var(--navy)}
.foot-head{font-size:27px;color:#fff;font-family:'League Spartan',sans-serif;font-weight:600}
.foot-links{left:116px;top:4860px;list-style:none;color:#fff;font-size:15px;line-height:34px}
.socials{left:112px;top:5068px;display:flex;gap:8px}
.socials span{width:26px;height:26px;border-radius:50%;background:var(--blue);display:block}
.divider{border-left:2px dotted #4a5568}
.contact-row{left:437px;display:flex;gap:16px;color:#fff;font-size:15px;line-height:24px}
.contact-row b{display:block}
.ring{width:44px;height:44px;border-radius:50%;border:2px solid var(--blue);display:flex;align-items:center;justify-content:center;flex:none}
.field{left:814px;width:272px;height:44px;background:#fff;border-radius:3px;font-size:14px;color:#8a8f99;padding:13px 16px}
.submit{left:814px;top:5052px;width:272px;height:44px;font-size:15px;border-radius:2px}
.copy{left:0;top:5167px;width:1200px;height:59px;background:var(--blue);color:#fff;font-size:14px;display:flex;align-items:center;justify-content:center}
</style>
</head>
<body>

<svg class="shapes" width="1200" height="5226" viewBox="0 0 1200 5226" aria-hidden="true">
  <!-- nav bar -->
  <rect x="0" y="72" width="1200" height="54" fill="var(--blue)"/>
  <polygon points="893,72 1200,72 1200,126 873,126" fill="var(--navy)"/>
  <!-- hero base with border -->
  <polygon points="0,126 1200,126 1200,652 812,846 0,622" fill="var(--blue)"/>
  <!-- control frame -->
  <rect x="158" y="914" width="360" height="352" fill="none" stroke="#cfe0f3" stroke-width="10"/>
  <rect x="106" y="1090" width="300" height="234" fill="var(--blue)"/>
  <!-- lighten section -->
  <polygon points="0,1700 386,1516 1200,1690 1200,2180 0,2180" fill="var(--blue)"/>
  <polygon points="0,1716 386,1534 1200,1700 1200,2180 0,2180" fill="var(--pale)"/>
  <!-- band -->
  <rect x="0" y="2178" width="1200" height="350" fill="var(--blue)"/>
  <rect x="0" y="2178" width="1200" height="350" fill="url(#bandShade)"/>
  <!-- allows section -->
  <polygon points="0,2527 1200,2527 1200,3048 812,3170 0,3012" fill="var(--blue)"/>
  <polygon points="0,2527 1200,2527 1200,3036 812,3156 0,2998" fill="var(--pale)"/>
  <!-- dotted decoration -->
  <g fill="#b7bcc6">
    <circle cx="84" cy="3560" r="2"/><circle cx="96" cy="3560" r="2"/><circle cx="84" cy="3574" r="2"/><circle cx="96" cy="3574" r="2"/>
    <circle cx="84" cy="3588" r="2"/><circle cx="96" cy="3588" r="2"/><circle cx="84" cy="3602" r="2"/><circle cx="96" cy="3602" r="2"/>
    <circle cx="84" cy="3616" r="2"/><circle cx="96" cy="3616" r="2"/><circle cx="84" cy="3630" r="2"/><circle cx="96" cy="3630" r="2"/>
    <circle cx="84" cy="3644" r="2"/><circle cx="96" cy="3644" r="2"/><circle cx="84" cy="3658" r="2"/><circle cx="96" cy="3658" r="2"/>
    <circle cx="110" cy="3658" r="2"/><circle cx="124" cy="3658" r="2"/><circle cx="138" cy="3658" r="2"/><circle cx="152" cy="3658" r="2"/>
    <circle cx="166" cy="3658" r="2"/><circle cx="180" cy="3658" r="2"/><circle cx="194" cy="3658" r="2"/><circle cx="208" cy="3658" r="2"/>
    <circle cx="222" cy="3658" r="2"/><circle cx="236" cy="3658" r="2"/><circle cx="250" cy="3658" r="2"/>
  </g>
  <!-- after-sales section -->
  <polygon points="0,3910 386,3728 1200,3852 1200,4263 0,4263" fill="var(--navy)"/>
  <polygon points="0,3926 386,3746 1200,3866 1200,4263 0,4263" fill="var(--blue)"/>
  <!-- footer dividers drawn via html -->
  <defs>
    <linearGradient id="bandShade" x1="0" y1="0" x2="1" y2="1">
      <stop offset="0" stop-color="#1b7fd0" stop-opacity=".6"/>
      <stop offset="1" stop-color="#0a5aa3" stop-opacity=".6"/>
    </linearGradient>
  </defs>
</svg>

<!-- header -->
<div class="abs brand">Precise Finish Emulator</div>
<div class="abs phone-top">
  <span class="icon-circle"><svg width="16" height="16" viewBox="0 0 24 24"><path fill="#fff" d="M6.6 10.8a15.1 15.1 0 0 0 6.6 6.6l2.2-2.2a1 1 0 0 1 1-.25 11.4 11.4 0 0 0 3.6.57 1 1 0 0 1 1 1V20a1 1 0 0 1-1 1A17 17 0 0 1 3 4a1 1 0 0 1 1-1h3.5a1 1 0 0 1 1 1c0 1.25.2 2.45.57 3.57a1 1 0 0 1-.25 1z"/></svg></span>
  +41 79 000 12 34
</div>
<nav class="abs nav-links">
  <span class="active">Home</span><span>About</span><span>Our Services</span><span>Partners</span><span>Reference</span><span>Contact Us</span>
</nav>
<div class="abs login">LOGIN/SIGN UP
  <svg width="14" height="14" viewBox="0 0 24 24"><path fill="#fff" d="M10 17l1.4-1.4L8.8 13H20v-2H8.8l2.6-2.6L10 7l-5 5zM14 3h6v18h-6v-2h4V5h-4z"/></svg>
</div>

<!-- hero -->
<div class="abs" role="img" aria-label="Hand holding a smartphone with glowing chat bubbles and a small robot assistant on a dark background"
  style="left:0;top:126px;width:1200px;height:700px;clip-path:polygon(0 0,100% 0,100% 73%,67.7% 100%,0 69.5%);background:radial-gradient(ellipse at 75% 55%,#3a4c66 0%,#1c2638 45%,#0e1522 100%)"></div>
<h1 class="abs hero-title">Precise Finish<br>Emulator</h1>
<p class="abs hero-sub">Virtual Reality At The Service Of<br>Controlled Aesthetic Watchmaking.</p>
<div class="abs btn hero-btn">Read More
  <svg width="18" height="18" viewBox="0 0 24 24"><circle cx="12" cy="12" r="11" fill="#fff"/><path d="M10 7l5 5-5 5" stroke="var(--blue)" stroke-width="3" fill="none"/></svg>
</div>

<!-- aesthetic control -->
<div class="abs" role="img" aria-label="Team of colleagues reviewing documents together in a bright office" style="left:126px;top:946px;width:358px;height:348px;background:linear-gradient(135deg,#c9b9a4,#7e8a7c 55%,#5a4f49)"></div>
<h2 class="abs control-head">Aesthetic Control: How<br>To Control It?</h2>
<ul class="abs ticks">
  <li>Adopting a simple and unambiguous language for a common understanding of aesthetic quality at the extended enterprise level.</li>
  <li>By using a semantic reference matrix associating the types ofanomalies (scratches, marks, deformations, stains, etc.) with theintensity levels defined with the company.</li>
  <li>Determining the compliance thresholds of the component or product.</li>
  <li>Providing uniform training in operational competence for those responsible for aesthetic control.</li>
  <li>By designing realistic and attractive teaching sequences for total quality control.</li>
  <li>By regularly assessing the competence to measure the aesthetics, expressed in a tangible, reliable and sustainable way (R&amp;R), of a component or product.</li>
</ul>

<!-- lighten -->
<h2 class="abs center-head" style="top:1696px">Lighten the management of<br>physical components</h2>
<div class="abs para" style="left:112px;top:1824px;width:446px;text-align:justify">
  <p style="margin-bottom:8px">Companies must manage and maintain sets of physical components used as a "yardstick" for the training of aesthetic testers.</p>
  <p style="margin-bottom:8px">The cost of managing a set of physical parts representing all combinations of shapes, defect types, materials and finishes is very high.</p>
  <p>PFE allows the company to significantly reduce its management burden by scanning components or products in 3D and then virtually adding 'typical' aesthetic anomalies.</p>
</div>
<div class="abs" role="img" aria-label="Cheerful business team celebrating around a laptop" style="left:607px;top:1829px;width:480px;height:252px;border-radius:4px;background:linear-gradient(120deg,#d9dde2,#8d99a8 50%,#3e4a5c)"></div>

<!-- band -->
<h2 class="abs center-head" style="top:2232px;color:#fff">Raising awareness of criteria<br>and aesthetic vocabulary</h2>
<div class="abs band-text" style="top:2348px">
  <p style="margin-bottom:24px">Aesthetic defects are often the result of careless handling of the components and products concerned, whether during manufacture, assembly or marketing.</p>
  <p>By making the PFE platform available to staff in direct contact with the product, it becomes very easy to make them aware of the evaluation criteria and the aesthetic vocabulary defined by the company.</p>
</div>

<!-- allows -->
<h2 class="abs center-head" style="top:2598px">PFE Allows</h2>
<div class="abs card" style="left:112px;top:2696px;width:229px;height:238px">
  <svg width="86" height="86" viewBox="0 0 86 86" fill="none" stroke="var(--blue)" stroke-width="2.5"><circle cx="34" cy="46" r="18"/><circle cx="34" cy="46" r="7"/><circle cx="60" cy="24" r="12"/><circle cx="60" cy="24" r="4"/><circle cx="62" cy="62" r="10"/><circle cx="62" cy="62" r="3"/></svg>
  Remove the management of components used as standards for aesthetic control training
</div>
<div class="abs card" style="left:361px;top:2696px;width:229px;height:238px">
  <svg width="86" height="86" viewBox="0 0 86 86" fill="none" stroke="var(--blue)" stroke-width="2.5"><circle cx="32" cy="18" r="8"/><circle cx="54" cy="18" r="8"/><path d="M18 44c0-10 8-14 14-14s11 3 11 8c0-5 5-8 11-8s14 4 14 14"/><path d="M10 62l20-8 16 4 20-10M14 74l20-6 24 2"/></svg>
  To make employees aware of aesthetic control and the vocabulary to be used
</div>
<div class="abs card" style="left:610px;top:2696px;width:229px;height:238px">
  <svg width="86" height="86" viewBox="0 0 86 86" fill="none" stroke="var(--blue)" stroke-width="2.5"><circle cx="43" cy="30" r="20"/><circle cx="43" cy="30" r="8"/><circle cx="18" cy="62" r="7"/><circle cx="43" cy="62" r="7"/><circle cx="68" cy="62" r="7"/><path d="M8 82c0-6 4-9 10-9s10 3 10 9M33 82c0-6 4-9 10-9s10 3 10 9M58 82c0-6 4-9 10-9s10 3 10 9"/></svg>
  Integrate aesthetic control into a total quality management (TQM) approach with precise indicators at all stages
</div>
<div class="abs card" style="left:859px;top:2696px;width:229px;height:238px">
  <svg width="86" height="86" viewBox="0 0 86 86" fill="none" stroke="var(--blue)" stroke-width="2.5"><circle cx="48" cy="28" r="18"/><path d="M42 22l12 12M54 22L42 34"/><path d="M8 60h14l14 6h18l14-10M8 76h16l14 4 32-16"/></svg>
  Provide the after-sales service with anefficient tool to record the aestheticaspect of the supported product
</div>

<!-- simulator -->
<div class="abs" role="img" aria-label="Overhead view of a business team meeting around a wooden table" style="left:112px;top:3273px;width:474px;height:376px;box-shadow:0 6px 24px rgba(20,40,80,.2);background:linear-gradient(135deg,#d7d9dc,#9a8770 50%,#4a4540)"></div>
<h2 class="abs" style="left:668px;top:3296px;font-size:42px;line-height:48px">Precise Finish<br>Emulator</h2>
<p class="abs para" style="left:668px;top:3416px;width:418px;text-align:justify">Norvik Works has developed, in collaboration with the Lakeside watchmaking school, a fault simulator on a mechanical part. This allows teachers to train students in more depth in the profession of quality controller. This tool combined with an LMS (Learning Management System) or the integrated management interface makes it possible to animate aesthetic control training in a fun and efficient way. Here is the product brochure while waiting for the dedicated site.</p>

<!-- after-sales -->
<h2 class="abs center-head" style="top:3912px;color:#fff">Improve after-sales service returns</h2>
<div class="abs band-text" style="top:3986px;left:210px;width:780px">
  <p style="margin-bottom:16px">The PFE platform can easily be used by the service network staff to assist them in the objective assessment of aesthetic defects by referring to the semantic matrix as well as to the cases already referenced.</p>
  <p>It is also possible, in an intuitive and playful way, to indicate, in accordance with the product nomenclature, a type of imperfection, its intensity and its location. It is also possible to draw up a precise repair estimate or to declare a non-conformity on a product coming from a market return.</p>
</div>
<div class="abs story-card" style="left:126px;top:4182px;width:459px;height:436px">
  <div role="img" aria-label="Group of business people talking in a large hall" style="margin:14px 14px 0;height:270px;background:linear-gradient(135deg,#e4e6e8,#8b95a3 55%,#3b4454)"></div>
  <h3>Improving the total quality<br>approach</h3>
  <div class="more">Read More <svg width="17" height="17" viewBox="0 0 24 24"><circle cx="12" cy="12" r="11" fill="var(--blue)"/><path d="M10 7l5 5-5 5" stroke="#fff" stroke-width="3" fill="none"/></svg></div>
</div>
<div class="abs story-card" style="left:615px;top:4182px;width:459px;height:436px">
  <div role="img" aria-label="Colleagues working at desks in a modern bright office" style="margin:14px 14px 0;height:270px;background:linear-gradient(135deg,#eef0f2,#a9b3bf 55%,#5a6676)"></div>
  <h3>A semantic matrix of aesthetic<br>defects</h3>
  <div class="more">Read More <svg width="17" height="17" viewBox="0 0 24 24"><circle cx="12" cy="12" r="11" fill="var(--blue)"/><path d="M10 7l5 5-5 5" stroke="#fff" stroke-width="3" fill="none"/></svg></div>
</div>

<!-- footer -->
<footer class="abs footer"></footer>
<div class="abs foot-head" style="left:112px;top:4782px">Quick links</div>
<ul class="abs foot-links">
  <li>Home</li><li>About</li><li>Our Services</li><li>Partners</li><li>Reference</li><li>Contact Us</li>
</ul>
<div class="abs socials"><span></span><span></span><span></span><span></span></div>
<div class="abs divider" style="left:392px;top:4850px;height:260px"></div>
<div class="abs foot-head" style="left:437px;top:4782px">Contact Details</div>
<div class="abs contact-row" style="top:4858px">
  <span class="ring"><svg width="20" height="20" viewBox="0 0 24 24" fill="none" stroke="var(--blue)" stroke-width="2"><circle cx="12" cy="12" r="9"/><path d="M3 12h18M12 3c3 3 3 15 0 18M12 3c-3 3-3 15 0 18"/></svg></span>
  <div><b>Emaill</b>hello@norvik-works.ch</div>
</div>
<div class="abs" style="left:437px;top:4932px;width:280px;border-top:2px dotted #4a5568"></div>
<div class="abs contact-row" style="top:4958px">
  <span class="ring"><svg width="18" height="18" viewBox="0 0 24 24"><path fill="var(--blue)" d="M6.6 10.8a15.1 15.1 0 0 0 6.6 6.6l2.2-2.2a1 1 0 0 1 1-.25 11.4 11.4 0 0 0 3.6.57 1 1 0 0 1 1 1V20a1 1 0 0 1-1 1A17 17 0 0 1 3 4a1 1 0 0 1 1-1h3.5a1 1 0 0 1 1 1c0 1.25.2 2.45.57 3.57a1 1 0 0 1-.25 1z"/></svg></span>
  <div><b>Phone</b>+41 79 000 12 34</div>
</div>
<div class="abs" style="left:437px;top:5030px;width:280px;border-top:2px dotted #4a5568"></div>
<div class="abs contact-row" style="top:5048px">
  <span class="ring"><svg width="18" height="18" viewBox="0 0 24 24"><path fill="var(--blue)" d="M6.6 10.8a15.1 15.1 0 0 0 6.6 6.6l2.2-2.2a1 1 0 0 1 1-.25 11.4 11.4 0 0 0 3.6.57 1 1 0 0 1 1 1V20a1 1 0 0 1-1 1A17 17 0 0 1 3 4a1 1 0 0 1 1-1h3.5a1 1 0 0 1 1 1c0 1.25.2 2.45.57 3.57a1 1 0 0 1-.25 1z"/></svg></span>
  <div><b>Phone</b>+41 79 000 56 78</div>
</div>
<div class="abs divider" style="left:757px;top:4850px;height:260px"></div>
<div class="abs foot-head" style="left:814px;top:4780px">Contact Me</div>
<div class="abs field" style="top:4838px">Name:</div>
<div class="abs field" style="top:4892px">Email:</div>
<div class="abs field" style="top:4946px">Phone:</div>
<div class="abs field" style="top:5000px">Message:</div>
<div class="abs btn submit">SUBMIT NOW</div>
<div class="abs copy">© 2023 &nbsp;Precise Finish Emulator.All rights reserved.</div>

</body>
</html>
```